Integrated Vertebral Clinic of Dallas
Spine center
Health
I am a spine surgeon in Dallas looking to create my first website. I do complex spine surgery on all types of people.
Exciting
my logo is dark blue
yellow ascents
red accents
top
www.maplecrestortho.example
www.hollowayneuroandback.example
i really like the drop down boxes in the holloway site but I like the look of the maplecrest ortho site
logo in tiff
photo
words for home page
logo
new written body
office

```html
<!DOCTYPE html>
<html lang="en">
<head>
<meta charset="utf-8">
<title>Integrated Vertebral Clinic of Dallas</title>
<link href="https://fonts.googleapis.com/css2?family=Arimo:wght@400;700&family=PT+Serif:wght@700&display=swap" rel="stylesheet">
<style>
:root{
  --bg-deep:#0f2a5c;
  --bg-mid:#1c3f7d;
  --navy:#1a3566;
  --orange:#f07a1a;
  --orange-dark:#d9600a;
  --white:#ffffff;
  --text:#333a45;
  --muted:#6c7480;
  --box:#e6edf5;
  --box-head:#d2dcea;
  --link:#1d4f9a;
  --hero-blue:#2c5f9e;
}
*{margin:0;padding:0;box-sizing:border-box}
html,body{width:1200px;height:952px;overflow:hidden}
body{background:radial-gradient(ellipse at 50% 30%,var(--bg-mid),var(--bg-deep) 75%);font-family:"Arimo",Arial,sans-serif;color:var(--text);position:relative}
.page{position:absolute;left:244px;top:26px;width:712px}
.header{height:98px;background:var(--white);border-radius:8px 8px 0 0;position:relative}
.brand{position:absolute;left:22px;top:26px;display:flex;align-items:center;gap:10px}
.brand-dot{width:34px;height:34px;border-radius:50%;background:var(--navy)}
.brand-name{font-family:"PT Serif",Georgia,serif;font-weight:700;color:var(--navy);font-size:19px;line-height:1.1;width:240px}
.appt{position:absolute;right:22px;top:24px;text-align:right}
.appt small{display:block;color:var(--orange);font-size:12px;font-style:italic;font-weight:700}
.appt .phone{display:flex;align-items:center;gap:8px;color:var(--navy);font-size:30px;font-weight:700;margin-top:2px}
.nav{height:36px;background:linear-gradient(var(--orange),var(--orange-dark));display:flex;align-items:center;justify-content:space-around;padding:0 10px}
.nav a{color:var(--white);font-size:12px;font-weight:700;text-decoration:none}
.hero{height:183px;position:relative;display:flex}
.hero-photo{width:440px;height:100%;background:linear-gradient(120deg,#9a8a78,#c9b9a4 45%,#5b6d86);position:relative}
.dots{position:absolute;left:168px;bottom:14px;display:flex;gap:6px}
.dots span{width:8px;height:8px;border-radius:50%;background:var(--white);opacity:.6}
.dots span:first-child{opacity:1;background:var(--orange)}
.hero-panel{flex:1;background:linear-gradient(160deg,#4c83bf,var(--hero-blue));color:var(--white);padding:18px 16px}
.hero-panel h2{font-size:14px;font-weight:700;letter-spacing:.5px;line-height:1.25}
.hero-panel p{font-size:10px;line-height:1.4;margin-top:8px}
.btn{display:inline-flex;align-items:center;gap:8px;margin-top:18px;background:var(--navy);color:var(--white);font-size:12px;font-weight:700;padding:7px 8px 7px 14px;border-radius:14px}
.btn i{width:16px;height:16px;border-radius:50%;background:var(--white);display:inline-block;position:relative}
.welcome{background:var(--white);height:212px;position:relative;padding:14px 150px 0 14px}
.welcome h1{font-family:"PT Serif",Georgia,serif;font-size:17px;color:var(--navy);display:flex;align-items:center;gap:8px}
.welcome h1 b{width:16px;height:16px;border-radius:50%;background:var(--orange);display:inline-block}
.welcome p{font-size:9.5px;line-height:1.35;margin-top:8px;color:var(--text)}
.doctor{position:absolute;right:8px;top:10px;width:118px;height:198px;background:linear-gradient(#dfe5ec,#8a97a8)}
.doctor-name{position:absolute;right:60px;top:2px;font-size:9px;color:var(--muted)}
.boxes{display:flex;gap:13px;margin-top:8px}
.box{flex:1;height:165px;background:var(--box);border-radius:6px;position:relative;padding:0 10px}
.box h3{display:flex;align-items:center;gap:8px;height:30px;border-bottom:1px solid var(--box-head);color:var(--navy);font-size:15px}
.box h3 b{width:14px;height:14px;border-radius:50%;background:var(--orange);display:inline-block}
.box ul{list-style:none;margin-top:6px}
.box li{font-size:10px;padding:5px 0;border-bottom:1px dotted #b9c5d6}
.box li::before{content:"\203A";color:var(--orange);font-weight:700;margin-right:6px}
.box p{font-size:10px;line-height:1.35;margin-top:8px}
.writer{font-size:10px;font-weight:700;margin-top:6px}
.more{position:absolute;right:10px;bottom:8px;font-size:10px;color:var(--link)}
.news{display:flex;gap:8px;margin-top:8px}
.thumb{width:40px;height:38px;background:linear-gradient(#8ea3bd,#4d6482);flex:none}
.news .date{font-size:10px;font-weight:700;color:var(--navy)}
.news .txt{font-size:9px;line-height:1.3}
.footer{display:flex;margin-top:20px;color:var(--white);padding:0 4px}
.footer h4{color:var(--orange);font-size:13px;font-weight:700;margin-bottom:10px}
.fcol{font-size:9.5px;line-height:2}
.nav-cols{display:flex;gap:40px;width:260px}
.contact{display:flex;gap:36px;width:330px}
.contact table{border-collapse:collapse;font-size:9.5px}
.contact td{padding:2px 10px 5px 0}
.social{display:flex;gap:10px}
.social span{width:20px;height:20px;border-radius:50%;background:#4a8fd6}
.copyright{position:absolute;left:244px;top:900px;width:712px;height:24px;background:rgba(8,24,56,.7);color:#c7d2e4;font-size:9px;display:flex;align-items:center;justify-content:center}
</style>
</head>
<body>
<div class="page">
  <header class="header">
    <div class="brand"><span class="brand-dot"></span><span class="brand-name">Integrated Vertebral Clinic of Dallas</span></div>
    <div class="appt">
      <small>Schedule an Appointment?</small>
      <div class="phone">
        <svg width="22" height="22" viewBox="0 0 24 24"><path fill="#f07a1a" d="M6.6 10.8a15 15 0 0 0 6.6 6.6l2.2-2.2c.3-.3.7-.4 1-.2 1.1.4 2.3.6 3.6.6.6 0 1 .4 1 1V20c0 .6-.4 1-1 1A17 17 0 0 1 3 4c0-.6.4-1 1-1h3.5c.6 0 1 .4 1 1 0 1.3.2 2.5.6 3.6.1.3 0 .7-.2 1z"/></svg>
        214 555 0187
      </div>
    </div>
  </header>
  <nav class="nav"><a>Home</a><a>Our Doctors</a><a>Services</a><a>Patient Information</a><a>Media Center</a><a>Contact Us</a></nav>
  <section class="hero">
    <div class="hero-photo" role="img" aria-label="Photo of a doctor talking with an older patient">
      <div class="dots"><span></span><span></span><span></span><span></span></div>
    </div>
    <div class="hero-panel">
      <h2>LOREM IPSUM DOLOR SIT AMET, CONSECTETUR ADIPISICING ELIT</h2>
      <p>Lorem ipsum dolor sit amet, consectetur adipisicing elit, sed do eiusmod tempor incididunt ut labore et dolore magna aliqua.</p>
      <span class="btn">Request an Appointment <i></i></span>
    </div>
  </section>
  <section class="welcome">
    <h1><b></b>Welcome to Integrated Vertebral Clinic of Dallas</h1>
    <p>The Integrated Vertebral Clinic of Dallas has over 40 years of experience treating disorders of the spine. We are totally focused on relieving your pain. Here at Integrated Vertebral Clinic no problem is too big or too small.</p>
    <p>The doctor is in. You will always see the doctor in our clinic and you will never leave without all your questions answered. At every visit you will have a one-on-one consultation with a board certified physician who carefully listens to you and helps you craft a treatment plan suited to your needs.</p>
    <p>We believe in non-operative care for most patients but in the instances where spine surgery is required, rest assured that the Integrated Vertebral Clinic of Dallas will be able to help. We believe in the power of individual, one on one care. The most advanced surgical methods available anywhere are offered to you. These include minimally invasive spine surgery, motion preservation surgery, total disc replacement surgery, XLIF and intraoperative process monitoring, as well as the most advanced spinal fusion surgery. For a complete list of services please click here. What we promise is an individual treatment plan tailored to you.</p>
    <span class="doctor-name">Dr. Derek</span>
    <div class="doctor" role="img" aria-label="Portrait of Dr. Derek in a dark suit"></div>
  </section>
  <section class="boxes">
    <div class="box">
      <h3><b></b>Our Services</h3>
      <ul><li>Lorem ipsum dolor sit amet</li><li>consectetur adipisicing elit sed do</li><li>eiusmod tempor incididunt ut</li><li>labore et dolore magna aliqua</li><li>Ut enim ad minim veniam</li></ul>
      <span class="more">[Read More]</span>
    </div>
    <div class="box">
      <h3><b></b>Patient Testimonials</h3>
      <p>Lorem ipsum dolor sit amet, consectetur adipisicing elit, sed do eiusmod tempor incididunt ut labore et dolore magna aliqua. Ut enim ad minim veniam, quis nostrud exercitation ullamco laboris nisi ut aliquip ex ea commodo consequat.</p>
      <div class="writer">- Writer's Name</div>
      <span class="more">[Read More]</span>
    </div>
    <div class="box">
      <h3><b></b>News &amp; Events</h3>
      <div class="news"><div class="thumb" role="img" aria-label="News thumbnail"></div><div><div class="date">10-6-2011</div><div class="txt">Lorem ipsum dolor sit amet, consectetur adipisicing elit sed do eiusmod.</div></div></div>
      <div class="news"><div class="thumb" role="img" aria-label="Event thumbnail"></div><div><div class="date">20-7-2011</div><div class="txt">Lorem ipsum dolor sit amet, consectetur adipisicing elit sed do eiusmod.</div></div></div>
      <span class="more">[Read More]</span>
    </div>
  </section>
  <footer class="footer">
    <div>
      <h4>Navigation</h4>
      <div class="nav-cols">
        <div class="fcol">Home<br>Our Doctors<br>services<br>Patient information<br>Media Center</div>
        <div class="fcol">Sitemap<br>Media Center<br>Contact Us</div>
      </div>
    </div>
    <div>
      <h4>Contact Us</h4>
      <div class="contact">
        <div class="fcol">Address Line 1<br>Address Line 2<br>City, State,<br>Country.</div>
        <table><tr><td>Phone</td><td>: +1-123-456-7890</td></tr><tr><td>Fax</td><td>: +1-123-456-7890</td></tr><tr><td>Email</td><td>: info@vertebralclinic.example</td></tr></table>
      </div>
    </div>
    <div>
      <h4>Follow Us</h4>
      <div class="social"><span></span><span></span></div>
    </div>
  </footer>
</div>
<div class="copyright">Copyright © 2011. Integrated Vertebral Clinic of Dallas. All rights reserved.</div>
</body>
</html>
```